PennacottHoldings.com Website Design

Simple website using existing logo. See "free website" already up. Want something much more professional and dynamic. Purpose is to describe my business and give me a place to post and update projects as they move along. Need to be able to post links to other companies that my firm invests equity in.
Target Market(s)
Banks, Financial Advisors
Industry/Entity Type
It Professional
Number of Pages Required
4 page
Font styles to use
Sans Serif
Requirements
Must have
- Ability to add and edit projects so they appear in the order of most current to oldest.
Nice to have
- Page to blog and link to facebook page

```html
<!DOCTYPE html>
<html lang="en">
<head>
<meta charset="utf-8">
<title>PennacottHoldings.com</title>
<link href="https://fonts.googleapis.com/css2?family=Open+Sans:wght@400;600;700&family=Raleway:wght@400;600;700&display=swap" rel="stylesheet">
<style>
:root{
  --red:#d0161b;
  --red-dark:#a80f13;
  --ink:#2b2b2b;
  --muted:#7a7a7a;
  --light:#f2f2f2;
  --line:#e1e1e1;
  --dark:#1c1c1c;
  --darker:#141414;
  --white:#ffffff;
}
*{box-sizing:border-box;margin:0;padding:0}
html,body{width:1200px;height:2356px;overflow:hidden}
body{font-family:"Open Sans",Arial,sans-serif;color:var(--ink);background:var(--white);position:relative}
.wrap{width:1040px;margin:0 auto;position:relative}
h1,h2,h3,h4{font-family:"Raleway","Open Sans",sans-serif}

/* top bar */
.topbar{height:28px;border-bottom:1px solid var(--line);font-size:11px;color:var(--muted)}
.topbar .wrap{display:flex;justify-content:flex-end;align-items:center;height:28px;gap:18px}
.socials{display:flex;gap:6px}
.socials span{width:14px;height:14px;border-radius:50%;background:var(--red);display:block}
.contact-item{display:flex;align-items:center;gap:5px}

/* header */
.header{height:120px}
.header .wrap{display:flex;justify-content:space-between;align-items:center;height:120px}
.brand{display:flex;align-items:center;gap:10px}
.brand-mark{width:34px;height:34px;background:var(--red)}
.brand-name{font-family:"Open Sans",sans-serif;font-weight:700;font-size:22px;color:var(--red);line-height:1}
.nav{display:flex;gap:8px}
.nav a{font-size:12px;font-weight:600;color:var(--ink);text-decoration:none;padding:9px 14px;text-transform:uppercase;letter-spacing:.5px}
.nav a.active{border:1px solid var(--red);color:var(--red)}

/* hero */
.hero{height:556px;background:radial-gradient(circle at 65% 50%,#3a3a3a 0%,#1d1d1d 70%);position:relative;overflow:hidden}
.hero-photo{position:absolute;left:250px;top:0;width:380px;height:556px;background:linear-gradient(180deg,#5a5452 0%,#2a2a2d 55%,#151518 100%)}
.hero-copy{position:absolute;left:760px;top:200px;width:300px;text-align:center;color:var(--white)}
.hero-mark{width:64px;height:64px;background:var(--red);margin:0 auto 14px}
.hero-title{font-family:"Open Sans",sans-serif;font-size:30px;font-weight:400;color:var(--white);margin-bottom:14px}
.hero-copy p{font-size:12px;line-height:1.6;color:#d6d6d6}
.hero-arrow{position:absolute;top:258px;width:30px;height:40px;display:flex;align-items:center;justify-content:center}
.hero-arrow.left{left:30px}.hero-arrow.right{right:30px}

/* welcome */
.welcome{padding:40px 0 0;height:372px}
.welcome .wrap{display:flex;gap:26px}
.welcome-photo{width:232px;height:290px;background:linear-gradient(180deg,#c9ccd1 0%,#5b5e66 60%,#2d2f36 100%);border:6px solid var(--white);box-shadow:0 0 0 1px var(--line)}
.welcome-text{width:440px;padding-top:4px}
.welcome-text h2{font-size:26px;font-weight:600;color:var(--ink);line-height:1.1}
.welcome-text h3{font-size:34px;font-weight:700;color:var(--red);line-height:1.15;margin-bottom:16px}
.welcome-text p{font-size:12px;line-height:1.7;color:var(--muted);margin-bottom:12px}
.more{font-size:11px;font-weight:700;color:var(--red);text-transform:uppercase;text-decoration:none;display:inline-flex;align-items:center;gap:5px}
.testimonials{width:316px;padding-top:4px}
.testimonials h4{font-size:18px;font-weight:600;color:var(--ink);display:flex;align-items:center;gap:8px;margin-bottom:14px}
.quote{background:var(--light);padding:18px;font-size:12px;line-height:1.7;color:var(--muted);font-style:italic;position:relative}
.author{display:flex;align-items:center;gap:12px;margin-top:18px}
.avatar{width:46px;height:46px;border-radius:50%;background:linear-gradient(180deg,#b9b2ad,#444)}
.author span{font-size:12px;color:var(--ink)}
.author em{color:var(--muted);font-style:normal}
.dots{display:flex;gap:6px;margin:14px 0 0 58px}
.dots i{width:16px;height:16px;border:1px solid var(--line);display:block}

/* services */
.services{background:var(--light);height:320px;padding-top:40px}
.section-title{text-align:center;font-size:30px;font-weight:600;color:var(--red);letter-spacing:.5px}
.section-title::after{content:"";display:block;width:60px;height:2px;background:var(--red);margin:12px auto 0}
.service-row{display:flex;justify-content:space-between;margin-top:44px}
.service{width:310px}
.service-head{display:flex;align-items:center;gap:12px;margin-bottom:12px}
.service-icon{width:40px;height:40px;border-radius:50%;background:var(--red);display:flex;align-items:center;justify-content:center}
.service h4{font-size:16px;font-weight:600;color:var(--ink);font-family:"Open Sans",sans-serif}
.service p{font-size:11px;line-height:1.7;color:var(--muted);margin-bottom:10px}

/* press */
.press{padding-top:52px;height:500px}
.press-head{display:flex;justify-content:space-between;align-items:center}
.press-head h2{font-size:22px;font-weight:700;color:var(--ink)}
.pager{display:flex;gap:4px}
.pager span{width:26px;height:26px;background:var(--light);display:flex;align-items:center;justify-content:center}
.cards{display:flex;gap:20px;margin-top:28px}
.card{width:245px}
.card-img{height:180px}
.card-img.a{background:linear-gradient(160deg,#e9e9ea,#b7b9bd)}
.card-img.b{background:linear-gradient(160deg,#f1f1f1,#9a9da3)}
.card-img.c{background:linear-gradient(160deg,#f4f4f4,#d8d4d2)}
.card-img.d{background:linear-gradient(160deg,#7d8ea3,#2e3a4a)}
.card-date{font-size:12px;font-weight:700;color:var(--red);margin:14px 0 6px}
.card h5{font-size:13px;font-weight:600;color:var(--ink);margin-bottom:8px;font-family:"Open Sans",sans-serif}
.card p{font-size:11px;line-height:1.6;color:var(--muted);margin-bottom:10px}

/* partners */
.partners{background:var(--light);height:112px;margin-top:28px}
.partners .wrap{display:flex;justify-content:space-between;align-items:center;height:112px}
.partner{height:34px;background:#c7c7c7;opacity:.8}

/* footer */
.footer{background:var(--dark);height:220px;padding-top:28px;color:#b5b5b5}
.footer .wrap{display:flex;justify-content:space-between}
.footer h4{font-size:13px;font-weight:600;color:var(--white);margin-bottom:14px;font-family:"Open Sans",sans-serif;text-transform:uppercase}
.footer p,.footer li{font-size:11px;line-height:1.8}
.footer ul{list-style:none}
.foot-brand{width:230px}
.foot-brand .brand-name{font-size:18px;margin:6px 0 20px}
.foot-social{display:flex;gap:6px}
.foot-social span{width:18px;height:18px;border:1px solid #666;border-radius:50%;display:block}
.foot-contact{width:250px}
.foot-links{width:180px}
.signup{width:230px}
.field{height:30px;background:var(--white);margin-top:10px;font-size:11px;color:#999;padding:7px 10px}
.sub-row{display:flex;gap:8px;margin-top:10px}
.sub-row .field{margin:0;flex:1}
.btn{background:var(--red);color:var(--white);font-size:11px;font-weight:700;padding:8px 12px;text-transform:uppercase}
.copy{position:absolute;left:0;top:2300px;width:1200px;height:56px;background:var(--red);color:var(--white);font-size:11px;display:flex;align-items:center;justify-content:center}
</style>
</head>
<body>

<div class="topbar">
  <div class="wrap">
    <div class="socials"><span></span><span></span><span></span></div>
    <div class="contact-item">
      <svg width="10" height="10" viewBox="0 0 24 24"><path d="M6 2l4 4-2 3c1.5 3 4 5.5 7 7l3-2 4 4-3 4C10 21 3 14 2 5z" fill="#d0161b"/></svg>
      +1 555 014 2290
    </div>
    <div class="contact-item">
      <svg width="12" height="10" viewBox="0 0 24 18"><rect x="1" y="1" width="22" height="16" fill="none" stroke="#d0161b" stroke-width="2"/><path d="M1 1l11 9 11-9" fill="none" stroke="#d0161b" stroke-width="2"/></svg>
      info@pennacottholdings.com
    </div>
  </div>
</div>

<header class="header">
  <div class="wrap">
    <div class="brand"><span class="brand-mark"></span><span class="brand-name">Pennacott Holdings</span></div>
    <nav class="nav">
      <a class="active" href="#">Home</a><a href="#">About Us</a><a href="#">Our Services</a><a href="#">Press Release</a><a href="#">Contact Us</a>
    </nav>
  </div>
</header>

<section class="hero">
  <div class="hero-photo" role="img" aria-label="Portrait photo of a smiling businessman in a dark suit and red tie"></div>
  <div class="hero-copy">
    <div class="hero-mark"></div>
    <h1 class="hero-title">Pennacott Holdings</h1>
    <p>Steady capital and clear guidance for growing firms. We partner with owners who plan for the long run, and we stay beside them through each stage.</p>
  </div>
  <div class="hero-arrow left"><svg width="12" height="20" viewBox="0 0 12 20"><path d="M10 2L2 10l8 8" stroke="#fff" stroke-width="2" fill="none"/></svg></div>
  <div class="hero-arrow right"><svg width="12" height="20" viewBox="0 0 12 20"><path d="M2 2l8 8-8 8" stroke="#fff" stroke-width="2" fill="none"/></svg></div>
</section>

<section class="welcome">
  <div class="wrap">
    <div class="welcome-photo" role="img" aria-label="Portrait photo of the firm's founder in a suit"></div>
    <div class="welcome-text">
      <h2>WELCOME TO</h2>
      <h3>PENNACOTT HOLDINGS</h3>
      <p>Pennacott Holdings is a private equity firm focused on small and mid sized companies. We bring patient capital, hands on support and a wide network of partners to every business we back, helping owners reach the next stage of growth with confidence and care.</p>
      <p>Over the years our team has worked with founders, lenders and advisors across many sectors. We value trust, open talk and steady results over quick wins.</p>
      <a class="more" href="#">Read More <svg width="8" height="8" viewBox="0 0 10 10"><path d="M2 1l5 4-5 4" stroke="#d0161b" stroke-width="2" fill="none"/></svg></a>
    </div>
    <div class="testimonials">
      <h4><svg width="16" height="14" viewBox="0 0 20 16"><path d="M0 16V9c0-5 3-8 8-9v3c-3 1-4 3-4 5h4v8zm11 0V9c0-5 3-8 8-9v3c-3 1-4 3-4 5h4v8z" fill="#d0161b"/></svg>Testimonials</h4>
      <div class="quote">Working with this team gave our company the capital and the calm advice we needed. They listened first, then helped us plan a clear path for growth over the next five years.</div>
      <div class="author"><div class="avatar" role="img" aria-label="Client portrait photo"></div><span>Alan Reeve <em>- Manager</em></span></div>
      <div class="dots"><i></i><i></i></div>
    </div>
  </div>
</section>

<section class="services">
  <h2 class="section-title">OUR SERVICES</h2>
  <div class="wrap service-row">
    <div class="service">
      <div class="service-head"><div class="service-icon"><svg width="20" height="20" viewBox="0 0 20 20"><rect x="3" y="10" width="3" height="7" fill="#fff"/><rect x="8.5" y="6" width="3" height="11" fill="#fff"/><rect x="14" y="3" width="3" height="14" fill="#fff"/></svg></div><h4>Equity Capital</h4></div>
      <p>We invest growth equity in sound firms with strong teams, clear plans and room to expand in their markets.</p>
      <a class="more" href="#">Click Here <svg width="8" height="8" viewBox="0 0 10 10"><path d="M2 1l5 4-5 4" stroke="#d0161b" stroke-width="2" fill="none"/></svg></a>
    </div>
    <div class="service">
      <div class="service-head"><div class="service-icon"><svg width="20" height="20" viewBox="0 0 20 20"><rect x="2" y="6" width="16" height="11" fill="none" stroke="#fff" stroke-width="2"/><path d="M7 6V3h6v3" fill="none" stroke="#fff" stroke-width="2"/></svg></div><h4>Business Consulting</h4></div>
      <p>Our advisors help owners shape strategy, improve operations and prepare for lenders, partners and buyers.</p>
      <a class="more" href="#">Click Here <svg width="8" height="8" viewBox="0 0 10 10"><path d="M2 1l5 4-5 4" stroke="#d0161b" stroke-width="2" fill="none"/></svg></a>
    </div>
    <div class="service">
      <div class="service-head"><div class="service-icon"><svg width="20" height="20" viewBox="0 0 20 20"><circle cx="10" cy="7" r="4" fill="#fff"/><path d="M3 18c0-4 3-6 7-6s7 2 7 6z" fill="#fff"/></svg></div><h4>Mentoring</h4></div>
      <p>We pair leaders with seasoned mentors who share lessons from years of building and running companies.</p>
      <a class="more" href="#">Click Here <svg width="8" height="8" viewBox="0 0 10 10"><path d="M2 1l5 4-5 4" stroke="#d0161b" stroke-width="2" fill="none"/></svg></a>
    </div>
  </div>
</section>

<section class="press">
  <div class="wrap">
    <div class="press-head">
      <h2>PRESS RELEASE</h2>
      <div class="pager">
        <span><svg width="6" height="10" viewBox="0 0 6 10"><path d="M5 1L1 5l4 4" stroke="#777" stroke-width="1.5" fill="none"/></svg></span>
        <span><svg width="6" height="10" viewBox="0 0 6 10"><path d="M1 1l4 4-4 4" stroke="#777" stroke-width="1.5" fill="none"/></svg></span>
      </div>
    </div>
    <div class="cards">
      <article class="card"><div class="card-img a" role="img" aria-label="Photo of a businessman climbing red block steps"></div><div class="card-date">JULY 12, 2015</div><h5>New fund opens for regional firms</h5><p>A fresh round of capital now supports family owned firms across the region.</p><a class="more" href="#">Click Here</a></article>
      <article class="card"><div class="card-img b" role="img" aria-label="Photo of a man facing a chalk drawn growth chart"></div><div class="card-date">JULY 12, 2015</div><h5>Partner firm posts record growth</h5><p>One of our portfolio firms reports its best quarter since the deal closed.</p><a class="more" href="#">Click Here</a></article>
      <article class="card"><div class="card-img c" role="img" aria-label="Illustration of a rising red bar chart with arrow"></div><div class="card-date">JULY 12, 2015</div><h5>Annual review shows steady gains</h5><p>Our yearly report shows steady returns across each of our core holdings.</p><a class="more" href="#">Click Here</a></article>
      <article class="card"><div class="card-img d" role="img" aria-label="Photo of business people meeting in an office"></div><div class="card-date">JULY 12, 2015</div><h5>Advisory team adds two partners</h5><p>Two seasoned advisors join to grow our consulting and mentoring work.</p><a class="more" href="#">Click Here</a></article>
    </div>
  </div>
</section>

<section class="partners">
  <div class="wrap">
    <span class="partner" style="width:80px"></span>
    <span class="partner" style="width:100px"></span>
    <span class="partner" style="width:110px"></span>
    <span class="partner" style="width:110px"></span>
    <span class="partner" style="width:100px"></span>
    <span class="partner" style="width:120px"></span>
  </div>
</section>

<footer class="footer">
  <div class="wrap">
    <div class="foot-brand">
      <span class="brand-mark" style="display:block;width:28px;height:28px"></span>
      <div class="brand-name">Pennacott Holdings</div>
      <div class="foot-social"><span></span><span></span><span></span><span></span><span></span></div>
    </div>
    <div class="foot-contact">
      <h4>Contact Us</h4>
      <p>Mark Pennacott<br>1418 Alder Row, Suite 200<br>Fairhaven, OR 97000</p>
      <p style="margin-top:8px">+1 555 014 2290<br>info@pennacottholdings.com</p>
    </div>
    <div class="foot-links">
      <h4>Quick Links</h4>
      <ul><li>Home</li><li>About Us</li><li>Services</li><li>Press Release</li><li>Contact Us</li></ul>
    </div>
    <div class="signup">
      <h4>Sign Up To Receive Email</h4>
      <p>Get news and project updates sent straight to your inbox.</p>
      <div class="field">Enter Name</div>
      <div class="sub-row"><div class="field">Enter Email</div><div class="btn">Subscribe</div></div>
    </div>
  </div>
</footer>
<div class="copy">Copyright 2015 Pennacott Holdings</div>

</body>
</html>
```